Pellworth and Tasker Ranch Insurance

Would like you all to design a logo for our Business cards and possible letterhead.
This business provides Ranch insurance for folks in Texas, New Mexico, and Oklahoma

Ggood stuff everybody, be sure to include email and Mobil for both of us on all designs

Thanks

Hello All

Wanted to let you all know i am going to extend deadline a few days, and add some more $$ to the budget

Reason: Give everybody a bit ,more time, and I added more money

Appreciate all of yalls hard work, will review and provide feed back hopefully today, been a little whacky with the holidays and all

Industry/Entity Type

Business

```html
<!DOCTYPE html>
<html lang="en">
<head>
<meta charset="utf-8">
<title>Pellworth and Tasker — Business Card</title>
<link rel="stylesheet" href="https://fonts.googleapis.com/css2?family=Source+Sans+3:wght@400;600;700&display=swap">
<style>
  :root {
    --paper: #ffffff;
    --saddle: #5e3815;
    --earth: #2f2217;
    --ink: #2a2119;
  }
  * { margin: 0; padding: 0; box-sizing: border-box; }
  html, body {
    width: 1200px;
    height: 686px;
    overflow: hidden;
    background: var(--paper);
  }
  .card {
    position: relative;
    width: 1200px;
    height: 686px;
    background: var(--paper);
    font-family: "Source Sans 3", "Helvetica Neue", Arial, sans-serif;
    color: var(--ink);
  }
  .firm {
    position: absolute;
    left: 182px;
    top: 198px;
  }
  .firm-name {
    font-size: 35px;
    font-weight: 700;
    color: var(--saddle);
    line-height: 46px;
  }
  .firm-address {
    font-style: normal;
    font-size: 35px;
    font-weight: 400;
    line-height: 45.5px;
    margin-top: 0;
  }
  .firm-web {
    font-size: 25px;
    line-height: 32px;
    margin-top: 14px;
  }
  .contacts {
    position: absolute;
    left: 697px;
    top: 198px;
  }
  .contact + .contact { margin-top: 33px; }
  .contact-name {
    font-size: 25px;
    font-weight: 600;
    line-height: 33px;
  }
  .contact-line {
    font-size: 25px;
    font-weight: 400;
    line-height: 33px;
  }
  .footer-band {
    position: absolute;
    left: 0;
    bottom: 0;
    width: 1200px;
    height: 96px;
  }
</style>
</head>
<body>
  <div class="card">
    <section class="firm">
      <div class="firm-name">Pellworth and Tasker</div>
      <address class="firm-address">
        482 W Cedar Avenue<br>
        Ozona, TX 76943<br>
        325.555.0187
      </address>
      <div class="firm-web">www.pellworthandtasker.com</div>
    </section>

    <section class="contacts">
      <div class="contact">
        <div class="contact-name">T. Jo Tasker</div>
        <div class="contact-line">jo@pellworthandtasker.com</div>
        <div class="contact-line">Mobile: 325-555-0146</div>
      </div>
      <div class="contact">
        <div class="contact-name">Wade Pellworth</div>
        <div class="contact-line">pellworthw@brevix.com</div>
        <div class="contact-line">Mobile: 512-555-0178</div>
      </div>
    </section>

    <svg class="footer-band" viewBox="0 0 1200 96" aria-hidden="true">
      <rect x="0" y="0" width="1200" height="12" fill="var(--saddle)"/>
      <rect x="0" y="12" width="1200" height="84" fill="var(--earth)"/>
    </svg>
  </div>
</body>
</html>
```